依頼詳細
ロゴを添付致しますので、それを使用してデザインをご提案していただきたいと思います。
法人あるいは個人のお客様にお渡しするのに使用します。
角2と長3の2種をお願いします。
記載項目
事業内容:高齢者と障がい者の身元保証(生活支援・金銭管理・死後事務・葬送支援)
社名:一般社団法人ひなたケアネット
事業所:□長久手事務所 〒480-1192 長久手市桜ヶ丘2-418
□名古屋事務所 〒458-0899 名古屋市緑区柳原4-217(有限会社森川工芸商会内)
電話番号:0561-48-9027
URL:https://hinata-cn.com/(QRコードを配置)
希望イメージ
シンプル 複雑
単色 カラフル
暗い 明るい
日常 高級
遊び心 厳粛
未来的 伝統的
女性的 男性的
希望する色
青系、水色系、無彩色系
納品ファイル
• 高解像度JPG (.jpg)
• イラストレーター形式 (.ai)
• フォトショップ形式 (.psd)
• PNG形式 (.png)
補足説明
記載項目は多少、アレンジいただいても大丈夫です。

色使いやデザインがイメージとあっていました。シンプルな中でも目に付きやすいデザインで気に入りました。

この度は素敵なデザインをありがとうございました。
どれも甲乙つけがたいくらい素晴らしいものが出そろって、正直悩みました。
また機会がありましたら宜しくお願い致します。
この度は誠にありがとうございました。重ねて御礼申し上げます。

```html
<!DOCTYPE html>
<html lang="ja">
<head>
<meta charset="utf-8">
<title>ひなたケアネット 長3封筒</title>
<link href="https://fonts.googleapis.com/css2?family=Noto+Sans+JP:wght@400;500;700&display=swap" rel="stylesheet">
<style>
  :root{
    --backdrop:#eeeeee;
    --paper:#ffffff;
    --sky:#7fc4ec;
    --sky-deep:#4fa9dd;
    --sky-pale:#d8eef9;
    --ink:#4a4a4a;
    --ink-soft:#6d6d6d;
  }
  *{margin:0;padding:0;box-sizing:border-box}
  html,body{width:846px;height:1200px;overflow:hidden;background:var(--backdrop);
    font-family:"Noto Sans JP",sans-serif;color:var(--ink)}
  .envelope{position:absolute;left:251px;top:124px;width:344px;height:953px;}
  .envelope__flap{position:absolute;left:0;top:0;width:344px;height:74px}
  .envelope__body{position:absolute;left:0;top:73px;width:344px;height:880px;background:var(--paper);
    box-shadow:0 2px 6px rgba(0,0,0,.12);overflow:hidden}
  .splash{position:absolute;left:0;top:0;width:344px;height:150px;
    background:linear-gradient(200deg,var(--sky) 0%,var(--sky-pale) 45%,rgba(255,255,255,0) 75%)}
  .identity{position:absolute;left:12px;top:612px;width:150px;display:flex;align-items:center;gap:6px}
  .identity__mark{width:26px;height:26px;border-radius:50%;background:var(--sky-deep);flex:none}
  .identity__name{font-size:9.5px;font-weight:500;color:var(--ink);line-height:1.25}
  .tagline{position:absolute;left:168px;top:614px;font-size:8px;color:var(--ink)}
  .services{position:absolute;left:168px;top:628px;display:flex;gap:2px}
  .services span{width:20px;height:20px;background:var(--sky-deep);color:#fff;font-size:5.5px;
    line-height:1.1;display:flex;align-items:center;justify-content:center;text-align:center;padding:1px}
  .phone{position:absolute;left:168px;top:652px;display:flex;align-items:center;gap:4px;
    font-size:17px;font-weight:700;color:var(--ink);letter-spacing:.02em}
  .phone svg{width:14px;height:14px}
  .url{position:absolute;left:12px;top:648px;font-size:7px;color:var(--ink-soft)}
  .footer-band{position:absolute;left:0;bottom:0;width:344px;height:182px;
    background:linear-gradient(180deg,var(--sky-pale) 0%,var(--sky) 35%,var(--sky) 100%)}
  .offices{position:absolute;left:12px;top:10px;width:320px;font-size:7px;color:var(--ink);line-height:1.6}
  .office{display:flex;gap:10px}
  .office__label{width:70px}
</style>
</head>
<body>
  <div class="envelope">
    <svg class="envelope__flap" viewBox="0 0 344 74" aria-hidden="true">
      <polygon points="4,0 340,0 344,74 0,74" fill="var(--sky)"/>
    </svg>
    <div class="envelope__body">
      <div class="splash" role="img" aria-label="水しぶきのような青い装飾模様"></div>

      <div class="identity">
        <div class="identity__mark"></div>
        <div class="identity__name">一般社団法人<br>ひなたケアネット</div>
      </div>
      <div class="url">https://hinata-cn.com/</div>

      <div class="tagline">高齢者と障がい者の身元保証</div>
      <div class="services">
        <span>生活<br>支援</span><span>金銭<br>管理</span><span>死後<br>事務</span><span>葬送<br>支援</span>
      </div>
      <div class="phone">
        <svg viewBox="0 0 24 24" aria-hidden="true"><path fill="var(--ink)" d="M6.6 10.8a15 15 0 0 0 6.6 6.6l2.2-2.2a1 1 0 0 1 1-.25 11.4 11.4 0 0 0 3.6.57 1 1 0 0 1 1 1V20a1 1 0 0 1-1 1A17 17 0 0 1 3 4a1 1 0 0 1 1-1h3.5a1 1 0 0 1 1 1 11.4 11.4 0 0 0 .57 3.6 1 1 0 0 1-.25 1z"/></svg>
        0561-48-9027
      </div>

      <div class="footer-band" role="img" aria-label="水しぶき模様の青い帯">
        <div class="offices">
          <div class="office"><span class="office__label">■長久手事務所</span><span>〒480-1192 長久手市桜ヶ丘2-418</span></div>
          <div class="office"><span class="office__label">■名古屋事務所</span><span>〒458-0899 名古屋市緑区柳原4-217<br>（有限会社森川工芸商会内）</span></div>
        </div>
      </div>
    </div>
  </div>
</body>
</html>
```